Aircraft maintenance buisness card

I am an aircraft mechanic looking for a personal buisness card . I would like my name and a title of Aircraft Maintenance Manager . I would like a suttle picture of an aircraft and helicopter .

elegant and professional wtih my contact .

My name should be on the car and Aircraft Maintenance Manager under with my contact infor below .

i have attached some pictures but i am open to other pics and ideas . I would like a airliner or private jet and a helicopter in the picture . The Images should be suttle and not the main idea . I also uploaded a picture of a jet engine which is cool . Be creative and i will work with you to finalize something .
Updates

Project Deadline Extended
Reason: Looking for more variations . Very good so far but looiking for a bit more styles and i uploaded my logo that i purchased . Please use my logo and be creative with it . I like some variations of black card with maybe some pictures that i uploaded but i am open to ideas . Be creative and i will work with you .

Project Deadline Extended
Reason: Looking for more designs and variations . Not yet satisfied with the designs i have gotten .

Industry/Entity Type

Aviation

Contact Information for Business Card

Aircraft Maintenance Manager

Font styles to use
Serif

Colors

Designer to choose colors to be used in the design.

Requirements
Must have
• An aviation related Logo if possible incorporated in the card possibly
• My name
• Tobias Marven Ellery
• 482 Pellow Ave.
• Brenmoor , PA
• 07519
• Email: Tmskyworks@quillmail.net
Nice to have
• Suttle Backround of a Private Jet or Airliner and a Helicopter .

```html
<!DOCTYPE html>
<html lang="en">
<head>
<meta charset="UTF-8">
<title>Tobias Marven Ellery – Aircraft Maintenance Manager</title>
<link href="https://fonts.googleapis.com/css2?family=Oswald:wght@500;600&family=Questrial&display=swap" rel="stylesheet">
<style>
  :root {
    --page-bg: #c9c9cb;
    --card-dark: #3b3c3f;
    --card-dark-edge: #333437;
    --sky-blue: #5fa8e2;
    --sky-blue-light: #7fbcec;
    --text-white: #f2f4f6;
    --photo-top: #4f78b8;
    --photo-mid: #a9c2e2;
    --photo-low: #e9eef5;
  }
  * { box-sizing: border-box; margin: 0; padding: 0; }
  html, body {
    width: 1200px; height: 809px; overflow: hidden;
    background: var(--page-bg);
  }
  .canvas {
    position: relative; width: 1200px; height: 809px;
    display: flex; justify-content: center; align-items: center; gap: 60px;
  }
  .card {
    position: relative; width: 330px; height: 578px;
    background: linear-gradient(160deg, var(--card-dark) 0%, var(--card-dark-edge) 100%);
    overflow: hidden;
    box-shadow: 0 10px 30px rgba(0,0,0,0.25);
  }

  /* Front */
  .title-band {
    position: absolute; top: 0; left: 0; right: 0; height: 88px;
    background: var(--sky-blue);
    display: flex; align-items: center; justify-content: center;
    text-align: center;
  }
  .job-title {
    font-family: "Oswald", sans-serif; font-weight: 500;
    color: var(--text-white); font-size: 23px; line-height: 1.2;
    letter-spacing: 1px; text-transform: uppercase;
  }
  .name {
    position: absolute; top: 238px; left: 22px; right: 22px;
    font-family: "Oswald", sans-serif; font-weight: 500;
    font-size: 21px; letter-spacing: 0.5px; text-transform: uppercase;
    text-align: right; color: var(--text-white);
  }
  .name .given { color: var(--sky-blue); }
  .name-rule {
    position: absolute; top: 276px; left: 22px; right: 22px;
    height: 2px; background: var(--sky-blue);
  }
  .contact-list {
    position: absolute; top: 302px; left: 26px; right: 16px;
    list-style: none;
    font-family: "Questrial", sans-serif; color: var(--text-white);
    font-size: 16px; line-height: 1.3;
  }
  .contact-list li {
    display: flex; align-items: flex-start; gap: 8px; margin-bottom: 9px;
  }
  .contact-icon { flex: 0 0 18px; width: 18px; height: 18px; margin-top: 1px; }
  .footer-band {
    position: absolute; left: 0; right: 0; bottom: 0; height: 128px;
    background: var(--sky-blue);
  }

  /* Back */
  .photo-strip {
    position: absolute; top: 160px; left: 0; right: 0; height: 238px;
    border-top: 6px solid var(--sky-blue);
    border-bottom: 6px solid var(--sky-blue);
  }
  .photo-fill {
    width: 100%; height: 100%;
    background: linear-gradient(180deg, var(--photo-top) 0%, var(--photo-mid) 45%, var(--photo-low) 75%, var(--photo-mid) 100%);
  }
</style>
</head>
<body>
  <main class="canvas">
    <section class="card card-front">
      <header class="title-band">
        <h1 class="job-title">Aircraft Maintenance<br>Manager</h1>
      </header>
      <h2 class="name"><span class="given">Tobias Marven</span> Ellery</h2>
      <div class="name-rule"></div>
      <ul class="contact-list">
        <li>
          <svg class="contact-icon" viewBox="0 0 18 18"><circle cx="9" cy="9" r="9" fill="#5fa8e2"/><circle cx="9" cy="9" r="4.5" fill="none" stroke="#3b3c3f" stroke-width="1.3"/><path d="M4.5 9h9M9 4.5c-2 2.5-2 6.5 0 9M9 4.5c2 2.5 2 6.5 0 9" fill="none" stroke="#3b3c3f" stroke-width="1"/></svg>
          <span>www.example.com</span>
        </li>
        <li>
          <svg class="contact-icon" viewBox="0 0 18 18"><circle cx="9" cy="9" r="9" fill="#5fa8e2"/><path d="M6 4.5l1.8 2.4-1 1.2c.7 1.3 1.6 2.2 2.9 2.9l1.2-1 2.4 1.8-1 1.7c-3.5-.4-6.8-3.7-7.2-7.2z" fill="#3b3c3f"/></svg>
          <span>000 000 0000</span>
        </li>
        <li>
          <svg class="contact-icon" viewBox="0 0 18 18"><circle cx="9" cy="9" r="9" fill="#5fa8e2"/><circle cx="9" cy="9" r="2" fill="none" stroke="#3b3c3f" stroke-width="1.3"/><path d="M11 7v3c0 1.5 2.3 1.5 2.3-.5A4.4 4.4 0 1 0 11 13" fill="none" stroke="#3b3c3f" stroke-width="1.3"/></svg>
          <span>Tmskyworks@quillmail.net</span>
        </li>
        <li>
          <svg class="contact-icon" viewBox="0 0 18 18"><circle cx="9" cy="9" r="9" fill="#5fa8e2"/><path d="M9 14.5s-3.6-4-3.6-6.4a3.6 3.6 0 0 1 7.2 0c0 2.4-3.6 6.4-3.6 6.4z" fill="#3b3c3f"/><circle cx="9" cy="8" r="1.3" fill="#5fa8e2"/></svg>
          <span>482 Pellow Ave, Brenmoor,<br>PA - 07519</span>
        </li>
      </ul>
      <footer class="footer-band"></footer>
    </section>

    <section class="card card-back">
      <div class="photo-strip">
        <div class="photo-fill" role="img" aria-label="Photograph of a white airliner flying head-on above clouds in a blue sky"></div>
      </div>
    </section>
  </main>
</body>
</html>
```